Systems and Technology Consultants - Website

Design & Build a website for a new company which operates in the Systems and Technology space for Transportation, Government and Commercial sectors.

Overall design should be minimalist in nature.
Should also have a feed that provides news and event updates on the main page.
Logo has already been awarded and should be incorporated into the site.

We like the overall layout, functionality and simplicity of the below sites. Submitted designs could be similar to or a combination of the aspects on these sites, or perhaps a whole different concept - we are open to new ideas.
Vortrane.com
Merp.it

Update 1 Dated 27 May 2014

All I am moving away from the Merp.it website and would like it to be more aligned with Vortrane.com not only in layout but in functionality. I will be extending the deadline of this design brief for two weeks to incorporate additional requirements and will add addtional funding to the project.

Apologies for not having more information available to provide but with so many submissions its getting confusing.

Thanks Dermot
Updates

Please note that the brief has been updated and the deadline has been extended.

Important: We will need two language versions of the website, English and Arabic; the website is hosted on HostPeak

Hello All, Thank you for your submissions. We have narrowed it down to the final 6 designers and I just wanted to take a moment and provide a bit of feedback regarding the concepts that we like and the modifications we are looking for. First, let me mention some of the design functions we like. - At the top of the homepage we really like the "region" or "language" tab so that the website can be viewed in both English and Arabic. - We like the homepage to have clear color variation so that the different sections of the homepage are distinct. Additionally, we like the bottom portion of the homepage to be in red. We feel that draws attention to our contact information. Again, we would like the colors to integrate black, gray-scale, red, etc. - Having a search tab at the top of the home page, or integrated into the main image, so that the site is easy to navigate. - We especially like the main image to have the scrolling tabs at the bottom so it is easy to browse the services offered (Consultancy, Solutions Architecture, Masters Systems Integration, Independent Design Review). - In regards to the services offered tab we really like the idea that a few people presented that have the outside of our logo with an icon in the middle of consultancy, solutions, etc., etc. Secondly, as mentioned in our brief we really enjoy the design of vortrane site. Specially, we enjoy the strong iconic images they use, the way the tabs at the top scroll easily, and contact us page that generates an email. Lastly, I've included some photos of the concept we have been working on. What we are trying to demonstrate is how our company offers a range of services that are essentially linked together. We provide individual services that when combined present the full service package. We would like this concept to be integrated into the over concept of our website. Please feel free to ask for clarification of any of the above points or contact us if you have any additional questions. We appreciate all of your hard work and are very excited to see the updated designs. Best, Miriam Dowbrook Plenvaro Senior Program Manager miriam.dowbrook@plenvaro-mail.com

Industry/Entity Type

Government

Font styles to use
Serif
Sans Serif

Requirements
Must have
• Must work on/adapt to various/mobile devices (responsive)
Must be simple and straightforward
Colors should be in line/matching with logo
2 language versions: English and Arabic (no Thai)
Services should be the first group/row of items after/below the main image
Note: the website will be hosted by hostpeak
Nice to have
• Submit feedback form
What's New section
The banner at the bottom of the site should not be too large; we would like a narrow one more
It would be nice if the header/top banner (with Home, About, etc. tabs) could stay in place as you scroll down (like Vortrane and Chatterly)
We will likely only use one image with a Company slogan on the Home page rather than a carousel of images to rotate through
Should not have
• This is the existing website: http://www.plenvaro-example.org
We do not like the animation, the way the banner icons/titles bounce
Not simple enough, we don't like the functionality or how pages load so slowly
We do not like the logo centered - it should be at the left
The banner and its tabs should not be towards the right, we would like them to be centered, to go all the way across and to be below the logo

```html
<!DOCTYPE html>
<html lang="en">
<head>
<meta charset="utf-8">
<title>Plenvaro International</title>
<link href="https://fonts.googleapis.com/css2?family=Arimo:wght@400;700&display=swap" rel="stylesheet">
<style>
:root{
  --red:#e8212b;
  --ink:#333333;
  --grey:#777777;
  --light:#999999;
  --band:#f1f1f1;
  --footer:#2f2f2f;
  --footer-dark:#262626;
  --bar:#1f1f1f;
  --white:#ffffff;
}
*{margin:0;padding:0;box-sizing:border-box}
html,body{width:898px;height:1200px;overflow:hidden;background:var(--white)}
body{font-family:"Arimo",Arial,sans-serif;color:var(--ink)}
h1,h2,h3{font-weight:400}
.page{position:relative;width:898px;height:1200px;overflow:hidden}
.abs{position:absolute}
.btn{position:absolute;background:var(--red);color:var(--white);font-size:7.5px;font-weight:700;display:flex;align-items:center;justify-content:center;letter-spacing:.2px;border-radius:2px;white-space:nowrap}

/* header */
.header{left:0;top:0;width:898px;height:58px;background:var(--white)}
.brand{left:186px;top:16px;display:flex;align-items:center;gap:8px}
.brand-mark{width:20px;height:20px;background:var(--red)}
.brand-name{color:var(--red);font-size:22px;font-weight:700;letter-spacing:2px}
.nav-item{top:24px;font-size:6.5px;color:var(--grey);white-space:nowrap}
.nav-item.active{color:var(--red);font-weight:700}
.nav-contact{left:656px;top:17px;width:57px;height:21px;font-size:6.5px}

/* hero */
.hero{left:0;top:58px;width:898px;height:280px;background:linear-gradient(180deg,#cfe4f3 0%,#5aa6dc 45%,#1a6fb5 75%,#2c86cf 100%)}
.hero-title{left:186px;top:170px;font-size:17px;font-weight:700;color:#222}
.hero-text{left:186px;top:201px;width:222px;font-size:8.5px;font-weight:700;line-height:11px;color:#111}
.hero-btn{left:186px;top:251px;width:59px;height:20px;font-size:6.5px}
.hero-card{left:541px;top:278px;width:172px;height:60px;background:rgba(120,150,175,.55)}
.hero-card-bar{left:541px;top:278px;width:142px;height:18px;background:var(--red);color:var(--white);font-size:6.5px;font-weight:700;padding:5px 0 0 13px;white-space:nowrap}
.hero-card-arrow{left:683px;top:278px;width:30px;height:18px;background:#3a3a3a}
.hero-card-text{left:554px;top:301px;width:150px;font-size:7.5px;line-height:9px;color:#1e2a36}
.hero-card-link{left:554px;top:325px;font-size:6.5px;font-weight:700;color:var(--white)}

/* intro */
.intro-lead{left:186px;top:389px;width:220px;font-size:11px;line-height:15px;color:var(--grey)}
.intro-body{left:439px;top:390px;width:274px;font-size:6.5px;line-height:11px;color:var(--light)}
.intro-btn{left:186px;top:456px;width:59px;height:21px;font-size:6.5px}
.intro-device{left:408px;top:438px;width:305px;height:68px}

/* services */
.services{left:0;top:506px;width:898px;height:166px;background:var(--band)}
.services-title{left:0;top:545px;width:898px;text-align:center;font-size:14px;color:var(--grey);letter-spacing:.5px}
.services-rule{top:553px;height:1px;background:#d4d4d4}
.service{top:590px;width:80px;text-align:center;font-size:7.5px;color:var(--grey)}
.service svg{display:block;margin:0 auto 7px}
.service.active{color:var(--red)}

/* news */
.news-title{left:0;top:702px;width:898px;text-align:center;font-size:14px;color:#555}
.news-card{top:750px;width:252px;height:142px}
.news-caption{position:absolute;left:0;right:0;text-align:center;font-size:8px;line-height:10px;color:var(--white);padding:0 30px}
.news-shade{position:absolute;left:0;right:0;bottom:0;height:46px;background:rgba(20,30,45,.55)}
.watch{position:absolute;left:96px;top:106px;width:60px;height:17px;background:var(--white);color:var(--red);font-size:6.5px;font-weight:700;display:flex;align-items:center;justify-content:center}
.news-btn{left:186px;top:918px;width:80px;height:23px;font-size:6.5px}

/* footer */
.footer{left:0;top:978px;width:898px;height:190px;background:var(--footer)}
.footer-panel{left:186px;top:978px;width:140px;height:190px;background:var(--footer-dark)}
.footer-brand{left:196px;top:1000px;display:flex;align-items:center;gap:6px}
.footer-brand .brand-mark{width:14px;height:14px}
.footer-brand .brand-name{font-size:15px}
.footer-address{left:198px;top:1035px;width:120px;font-size:6.5px;line-height:9px;color:#aaa}
.footer-map-label{left:198px;top:1066px;font-size:7px;color:#ccc;display:flex;align-items:center;gap:6px}
.footer-map{left:203px;top:1083px;width:98px;height:55px;background:#4a4a4a}
.footer-heading{top:1007px;font-size:9px;color:#e6e6e6}
.case{left:361px;width:120px;font-size:6.5px;line-height:8px;color:#bbb}
.case u{color:var(--white)}
.case .date{display:block;margin-top:4px;font-size:5.5px;color:#777}
.social{left:518px;font-size:6.5px;color:#aaa;display:flex;align-items:center;gap:9px}
.social i{width:5px;height:5px;border-radius:50%;background:#aaa;display:block}
.footer-email{left:518px;top:1087px;font-size:7.5px;color:var(--red)}
.bottom-bar{left:0;top:1168px;width:898px;height:32px;background:var(--bar)}
.bottom-text{left:186px;top:1184px;font-size:6.5px;color:#999}
</style>
</head>
<body>
<div class="page">

  <header class="abs header">
    <div class="abs brand"><span class="brand-mark"></span><span class="brand-name">PLENVARO</span></div>
    <nav>
      <span class="abs nav-item active" style="left:474px">HOME</span>
      <span class="abs nav-item" style="left:506px">ABOUT US</span>
      <span class="abs nav-item" style="left:553px">BUSINESS UNIT</span>
      <span class="abs nav-item" style="left:613px">SERVICES</span>
    </nav>
    <div class="btn nav-contact">CONTACT US</div>
  </header>

  <section class="abs hero" role="img" aria-label="Photograph of a blue steel arch bridge with a highway and trucks"></section>
  <h1 class="abs hero-title">System Design &amp; Engenering</h1>
  <p class="abs hero-text">Lorem Ipsum is simply dummy text of the printing and typesetting industry. Lorem Ipsum has been the industry's standard dummy text</p>
  <div class="btn hero-btn">VIEW DETAIL</div>
  <div class="abs hero-card"></div>
  <div class="abs hero-card-bar">Lorem Ipsum is simply dummy text</div>
  <div class="abs hero-card-arrow">
    <svg width="30" height="18" viewBox="0 0 30 18"><path d="M10 9h9M15 5l4 4-4 4" stroke="#fff" stroke-width="1.6" fill="none"/></svg>
  </div>
  <p class="abs hero-card-text">Lorem Ipsum is simply dummy text of the printing and typesetting</p>
  <span class="abs hero-card-link">CLICK HERE</span>

  <p class="abs intro-lead">Plenvaro International 30 years experience in engineering and construction of systems around the globe.</p>
  <p class="abs intro-body">Plenvaro is a joint venture between halvercrest construction, norvale worldwide and tessmark engineering &amp; management company founded in eastfield, northvale in 2003 and brindle electrical construction company founded in portmere, westhaven in 2001.</p>
  <div class="btn intro-btn">VIEW MORE</div>
  <div class="abs intro-device" role="img" aria-label="Laptop showing a yellow smartphone application page" style="background:linear-gradient(90deg,#cfcfcf 0%,#2b2b2b 12%,#f0c93a 40%,#f0c93a 95%,#2b2b2b 100%)"></div>

  <section class="abs services"></section>
  <h2 class="abs services-title">SERVICES OFFER</h2>
  <div class="abs services-rule" style="left:264px;width:106px"></div>
  <div class="abs services-rule" style="left:528px;width:106px"></div>
  <div class="abs" style="left:370px;top:550px;width:6px;height:6px;background:#ccc;transform:rotate(45deg)"></div>
  <div class="abs" style="left:522px;top:550px;width:6px;height:6px;background:#ccc;transform:rotate(45deg)"></div>

  <div class="abs service" style="left:270px">
    <svg width="24" height="24" viewBox="0 0 24 24"><circle cx="12" cy="12" r="11" fill="none" stroke="#444" stroke-width="1.5"/><path d="M7 9h3l4 6h3M7 15h3l4-6h3" stroke="#444" fill="none" stroke-width="1.2"/></svg>Consulting</div>
  <div class="abs service" style="left:339px">
    <svg width="24" height="24" viewBox="0 0 24 24"><circle cx="12" cy="12" r="11" fill="none" stroke="#444" stroke-width="1.5"/><path d="M12 6c2 2 2 6 1 9h-2c-1-3-1-7 1-9zM10 14l-2 3h2M14 14l2 3h-2" fill="#444"/></svg>Engineering</div>
  <div class="abs service" style="left:410px">
    <svg width="24" height="24" viewBox="0 0 24 24"><circle cx="12" cy="12" r="11" fill="none" stroke="#444" stroke-width="1.5"/><path d="M8 7v10h9M10 15v-4M12 15v-6M14 15v-3" stroke="#444" fill="none" stroke-width="1.3"/></svg>Construction</div>
  <div class="abs service" style="left:478px">
    <svg width="24" height="24" viewBox="0 0 24 24"><circle cx="12" cy="12" r="11" fill="none" stroke="#444" stroke-width="1.5"/><circle cx="12" cy="12" r="5" fill="#444"/><path d="M12 12V7a5 5 0 0 1 5 5z" fill="#fff"/></svg>Operations</div>
  <div class="abs service active" style="left:547px">
    <svg width="24" height="24" viewBox="0 0 24 24"><circle cx="12" cy="12" r="11" fill="none" stroke="#e8212b" stroke-width="1.5"/><path d="M9 7v10M15 7v10M8 7h2M14 7h2" stroke="#e8212b" fill="none" stroke-width="1.3"/></svg>Maintenance</div>

  <h2 class="abs news-title">IN THE NEWS</h2>
  <article class="abs news-card" style="left:186px;background:linear-gradient(135deg,#d9d6d2 0%,#8c8a86 55%,#2c2c30 100%)" role="img" aria-label="Photograph of a smiling businesswoman in an office">
    <p class="news-caption" style="top:80px">Lorem Ipsum is simply dummy text of the printing and typesetting industry</p>
    <div class="watch">WATCH VIDEO</div>
  </article>
  <article class="abs news-card" style="left:461px;background:linear-gradient(180deg,#4f7fb3 0%,#c9cdd1 45%,#e4e4e4 100%)" role="img" aria-label="Photograph of a young man in a white shirt in front of a modern building">
    <div class="news-shade"></div>
    <p class="news-caption" style="top:108px">Lorem Ipsum is simply dummy text of the printing and typesetting industry</p>
  </article>
  <div class="btn news-btn">OUR CUSTOMERS</div>

  <footer class="abs footer"></footer>
  <div class="abs footer-panel"></div>
  <div class="abs footer-brand"><span class="brand-mark"></span><span class="brand-name">PLENVARO</span></div>
  <p class="abs footer-address">12 larchmont rd, eastfield, northvale,<br>north district 40120</p>
  <div class="abs footer-map-label">
    <svg width="8" height="11" viewBox="0 0 8 11"><path d="M4 0a4 4 0 0 1 4 4c0 3-4 7-4 7S0 7 0 4a4 4 0 0 1 4-4z" fill="#ccc"/><circle cx="4" cy="4" r="1.5" fill="#262626"/></svg>Map It</div>
  <div class="abs footer-map" role="img" aria-label="Grey world map"></div>

  <h3 class="abs footer-heading" style="left:358px">CASE STUDIES</h3>
  <p class="abs case" style="top:1031px">Lorem Ipsum is <u>simply dummy text</u> of the printing and typesetting industry.<span class="date">25 June 2015</span></p>
  <p class="abs case" style="top:1066px">Lorem Ipsum is <u>simply dummy text</u> of the printing and typesetting industry.<span class="date">25 June 2015</span></p>
  <p class="abs case" style="top:1108px">Lorem Ipsum is <u>simply dummy text</u> of the printing and typesetting industry.<span class="date">25 June 2015</span></p>

  <h3 class="abs footer-heading" style="left:516px">GET IN TOUCH</h3>
  <p class="abs social" style="top:1031px"><i></i>chirper.com/plenvaro</p>
  <p class="abs social" style="top:1045px"><i></i>chatterly.com/pages/plenvaro</p>
  <p class="abs social" style="top:1059px"><i></i>linkpro.com/company/plenvaro</p>
  <p class="abs footer-email">Email: info@plenvaro-example.org</p>

  <div class="abs bottom-bar"></div>
  <p class="abs bottom-text">PLENVARO © 2014 &nbsp;|&nbsp; Terms &amp; Services &nbsp;|&nbsp; Privacy Policy</p>
</div>
</body>
</html>
```